New Flyer Design Project

Hi,
We were looking at a flyer for the testing run of the event. I have attached a design we like with comments on what to remove and add. Also attached is our logo. We want something with the same style and feel of the flyer attached and it suited the event we are running.
Thanks,
Colin
Colors
Designer to choose colors to be used in the design.

```html
<!DOCTYPE html>
<html lang="en">
<head>
<meta charset="utf-8">
<title>The Copper Ridge – Test Runners Required</title>
<link href="https://fonts.googleapis.com/css2?family=Montserrat:wght@500;700;800&display=swap" rel="stylesheet">
<style>
  :root {
    --page-bg: #ffffff;
    --brand-slate: #34525f;
    --accent-orange: #f07a28;
    --text-light: #ffffff;
    --sky-top: #4a6470;
    --sky-mid: #c9d6d3;
    --sky-glow: #eef0e6;
    --ground-light: #c8a860;
    --ground-mid: #8c7444;
    --ground-dark: #3f3120;
  }
  html, body {
    margin: 0;
    width: 1200px;
    height: 1200px;
    overflow: hidden;
    background: var(--page-bg);
    font-family: "Montserrat", Arial, sans-serif;
  }
  .flyer {
    position: absolute;
    left: 211px;
    top: 37px;
    width: 773px;
    height: 1093px;
    overflow: hidden;
  }
  .flyer-photo {
    position: absolute;
    inset: 0;
    background:
      radial-gradient(ellipse 320px 220px at 52% 58%, rgba(255,250,225,0.85), rgba(255,250,225,0) 70%),
      linear-gradient(180deg,
        var(--sky-top) 0%,
        #7f979b 20%,
        var(--sky-mid) 40%,
        var(--sky-glow) 56%,
        var(--ground-light) 59%,
        #a88d52 70%,
        var(--ground-mid) 82%,
        var(--ground-dark) 100%);
  }
  .social {
    position: absolute;
    top: 60px;
    right: 60px;
    display: flex;
    gap: 16px;
  }
  .social-item {
    display: flex;
    align-items: center;
    gap: 7px;
    color: var(--text-light);
    font-size: 15px;
    font-weight: 500;
  }
  .social-dot {
    width: 22px;
    height: 22px;
    border: 2px solid var(--text-light);
    border-radius: 50%;
    box-sizing: border-box;
  }
  .brand-mark {
    position: absolute;
    left: 284px;
    top: 112px;
    width: 206px;
    height: 206px;
    border-radius: 50%;
    background: var(--brand-slate);
  }
  .event-name {
    position: absolute;
    left: 0;
    right: 0;
    top: 340px;
    margin: 0;
    color: var(--brand-slate);
    font-weight: 700;
    text-align: center;
  }
  .event-name-kicker {
    display: flex;
    align-items: center;
    justify-content: center;
    gap: 40px;
    font-size: 40px;
    letter-spacing: 20px;
    line-height: 50px;
  }
  .event-name-kicker::before,
  .event-name-kicker::after {
    content: "";
    width: 190px;
    height: 5px;
    background: var(--brand-slate);
  }
  .event-name-kicker span { margin-right: -20px; }
  .event-name-main {
    margin-top: 6px;
    font-size: 72px;
    line-height: 80px;
    letter-spacing: 1px;
  }
  .callout {
    position: absolute;
    left: 162px;
    top: 517px;
    width: 459px;
    height: 45px;
    background: var(--accent-orange);
    color: var(--text-light);
    font-weight: 800;
    font-size: 27px;
    line-height: 45px;
    text-align: center;
    letter-spacing: 0.3px;
  }
  .event-date {
    position: absolute;
    left: 0;
    right: 0;
    top: 864px;
    color: var(--accent-orange);
    font-weight: 800;
    font-size: 50px;
    line-height: 56px;
    text-align: center;
    text-shadow: 0 2px 6px rgba(0,0,0,0.35);
  }
  .event-venue {
    position: absolute;
    left: 91px;
    top: 922px;
    width: 595px;
    height: 59px;
    background: var(--accent-orange);
    clip-path: polygon(0 0, 100% 0, 97% 100%, 3% 100%);
    color: var(--text-light);
    font-weight: 800;
    font-size: 45px;
    line-height: 60px;
    text-align: center;
  }
  .contact {
    position: absolute;
    left: 0;
    right: 0;
    top: 1008px;
    margin: 0;
    color: var(--text-light);
    font-size: 17px;
    font-weight: 500;
    text-align: center;
  }
</style>
</head>
<body>
  <main class="flyer">
    <div class="flyer-photo" role="img" aria-label="Mountain biker riding a wheelie across a sunlit rocky summit under a hazy teal sky"></div>

    <div class="social">
      <span class="social-item"><span class="social-dot"></span>Trailbook</span>
      <span class="social-item"><span class="social-dot"></span>Snapgram</span>
    </div>

    <div class="brand-mark" aria-hidden="true"></div>

    <h1 class="event-name">
      <div class="event-name-kicker"><span>THE</span></div>
      <div class="event-name-main">COPPER RIDGE</div>
    </h1>

    <div class="callout">TEST RUNNERS REQUIRED</div>

    <div class="event-date">15TH DECEMBER 2019</div>
    <div class="event-venue">AT MOUNT KALLORA</div>

    <p class="contact">Contact copperridgerace@trailmail.net or call 0400 123 456</p>
  </main>
</body>
</html>
```